Awesome photographers card for an awesome new business

Double sided business card Black background and silver logo in middle on one side. Details on otherside. please keep it simple

Photographer

Gavin Tolley
0482615073
GavinTolleyPhotography82@lumenpost.com
www.GavinTolleyPhotography.com.au
Instagram _Gavin_tolley

Requirements
Must have
• My logo in Silver
• please use instagram logo instead of "Instagram"

```html
<!DOCTYPE html>
<html lang="en">
<head>
<meta charset="utf-8">
<title>Gavin Tolley Photographer – Business Card</title>
<link href="https://fonts.googleapis.com/css2?family=Arimo:wght@400&display=swap" rel="stylesheet">
<style>
  :root {
    --page: #ffffff;
    --card: #000000;
    --ring: #5e5e5e;
    --ring-light: #7a7a7a;
    --ring-dark: #2e2e2e;
    --silver: #c9c9c9;
    --text: #d4d4d4;
    --icon: #8a8a8a;
  }
  * { margin: 0; padding: 0; box-sizing: border-box; }
  html, body {
    width: 1200px; height: 1200px; overflow: hidden;
    background: var(--page);
    font-family: "Arimo", Arial, sans-serif;
  }
  .card {
    position: absolute; left: 110px;
    width: 981px; height: 545px;
    background: var(--card);
    overflow: hidden;
  }
  .card--front { top: 20px; }
  .card--back { top: 621px; }
  .card__art { position: absolute; inset: 0; }
  .card__name {
    position: absolute; right: 23px; top: 26px;
    font-size: 38px; line-height: 1; color: var(--silver);
  }
  .card__role {
    position: absolute; right: 23px; top: 81px;
    font-size: 21px; line-height: 1; color: var(--text);
  }
  .brand-name {
    position: absolute; left: 490px; transform: translate(-50%, -50%);
    font-size: 30px; line-height: 1; color: var(--silver);
    white-space: nowrap;
  }
  .card--front .brand-name { top: 272px; }
  .card--back .brand-name { top: 271px; }
  .contact {
    position: absolute; top: 490px; height: 34px;
    display: flex; align-items: center; gap: 14px;
    font-size: 21px; color: var(--text); white-space: nowrap;
  }
  .contact--phone { left: 22px; }
  .contact--social { left: 234px; gap: 12px; }
  .contact--email { left: 478px; gap: 18px; font-size: 20px; }
  .contact__dot {
    width: 36px; height: 36px; border-radius: 50%;
    background: var(--icon);
  }
  .card__web {
    position: absolute; left: 0; right: 0; top: 456px;
    text-align: center; font-size: 18px; color: var(--text);
  }
</style>
</head>
<body>

<section class="card card--front">
  <svg class="card__art" width="981" height="545" viewBox="0 0 981 545">
    <defs>
      <linearGradient id="band-left" x1="0" x2="1" y1="0" y2="0">
        <stop offset="0" stop-color="#5a5a5a"/>
        <stop offset="0.6" stop-color="#3a3a3a"/>
        <stop offset="1" stop-color="#5e5e5e"/>
      </linearGradient>
    </defs>
    <rect class="band" x="0" y="241" width="490" height="63" fill="url(#band-left)"/>
    <rect class="band" x="490" y="241" width="491" height="63" fill="var(--ring)"/>
    <circle class="ring" cx="490" cy="272" r="172" fill="var(--ring)"/>
    <circle class="ring-inner" cx="490" cy="272" r="140" fill="var(--card)"/>
  </svg>

  <h1 class="card__name">Gavin Tolley</h1>
  <p class="card__role">Photographer</p>
  <p class="brand-name">Gavin Tolley</p>

  <div class="contact contact--phone">
    <svg width="36" height="36" viewBox="0 0 24 24" aria-hidden="true">
      <path fill="var(--icon)" d="M6.6 2.5c.5-.3 1.1-.2 1.4.3l2 3.2c.3.5.2 1.1-.2 1.4L8.4 8.5c.9 2.6 3.4 5.4 6 6.7l1.2-1.4c.4-.4 1-.5 1.4-.2l3.1 2c.5.3.6.9.3 1.4l-1.3 2.2c-.5.9-1.6 1.3-2.6 1C9.4 18.4 4.9 13.6 3.6 6.6c-.2-1 .3-2 1.1-2.5z"/>
    </svg>
    <span>0482615073</span>
  </div>

  <div class="contact contact--social">
    <span class="contact__dot"></span>
    <span>_Gavin_tolley</span>
  </div>

  <div class="contact contact--email">
    <svg width="38" height="30" viewBox="0 0 38 30" aria-hidden="true">
      <rect x="1.5" y="2.5" width="35" height="25" fill="none" stroke="var(--icon)" stroke-width="2"/>
      <polyline points="1.5,2.5 19,17 36.5,2.5" fill="none" stroke="var(--icon)" stroke-width="2"/>
    </svg>
    <span>GavinTolleyPhotography82@lumenpost.com</span>
  </div>
</section>

<section class="card card--back">
  <svg class="card__art" width="981" height="545" viewBox="0 0 981 545">
    <defs>
      <linearGradient id="ring-shade" x1="0" x2="1" y1="0" y2="1">
        <stop offset="0" stop-color="var(--ring-dark)"/>
        <stop offset="0.5" stop-color="var(--ring)"/>
        <stop offset="1" stop-color="var(--ring-light)"/>
      </linearGradient>
    </defs>
    <circle class="ring" cx="490" cy="271" r="160" fill="url(#ring-shade)"/>
    <circle class="ring-inner" cx="490" cy="271" r="136" fill="var(--card)"/>
  </svg>

  <p class="brand-name">Gavin Tolley</p>
  <p class="card__web">www.GavinTolleyPhotography.com.au</p>
</section>

</body>
</html>
```